Corvalen Technologies Support Business Card

I would like a business card that doesn't focus on an individual role within our company but rather and call to action for current and potential clients to engage with us. We are a small business hybrid IT support company out of Metro Detroit in Michigan. Something that contains a QR code as an easy way to seek support. It should include and simple call to action but also refers to our company values. "Experience is Everything" "Obsessed with Impossible" and "Consistency Over Time Equals Trust". Our brand colors are typically a deeper/darker read, black, charcoal and white. Please see our company logo attached, and our website is is www.corvalenpc.com

```html
<!DOCTYPE html>
<html lang="en">
<head>
<meta charset="utf-8">
<title>Corvalen Technologies Support Card</title>
<link rel="stylesheet" href="https://fonts.googleapis.com/css2?family=Courier+Prime:wght@400;700&family=Roboto+Slab:wght@300&display=swap">
<style>
  :root {
    --stage: #2b2b2d;
    --charcoal: #4a4a4c;
    --charcoal-ink: #333335;
    --charcoal-text: #c4c4c6;
    --paper: #ffffff;
    --ink: #2a2a2a;
    --brand-red: #8e1414;
    --edge-red: #7a0f0f;
  }
  * { box-sizing: border-box; margin: 0; padding: 0; }
  html, body { width: 1200px; height: 939px; overflow: hidden; }
  body { background: var(--stage); position: relative; font-family: "Courier Prime", monospace; }

  .card {
    position: absolute;
    width: 620px;
    height: 354px;
    border-bottom: 4px solid var(--edge-red);
    border-left: 2px solid var(--edge-red);
    box-shadow: 0 14px 30px rgba(0,0,0,0.45);
  }
  .card--back { left: 90px; top: 80px; background: var(--charcoal); }
  .card--front { left: 490px; top: 480px; background: var(--paper); }

  .wordmark {
    display: flex;
    align-items: center;
    gap: 14px;
    font-family: "Roboto Slab", serif;
    font-weight: 300;
    line-height: 0.95;
  }
  .wordmark__square { width: 16px; height: 16px; flex: none; }
  .wordmark__name span { display: block; }

  .card--back .wordmark {
    position: absolute; left: 50px; top: 56px;
    font-size: 46px; color: var(--charcoal-ink);
    text-shadow: 0 1px 0 rgba(255,255,255,0.08);
  }
  .card--back .wordmark__square { background: var(--charcoal-ink); width: 18px; height: 18px; }

  .values { position: absolute; left: 52px; top: 200px; list-style: none; color: var(--charcoal-text); }
  .values__title { font-size: 12px; letter-spacing: 2px; text-transform: uppercase; color: #e0a0a0; margin-bottom: 10px; }
  .values__item { display: flex; align-items: center; gap: 10px; font-size: 15px; line-height: 28px; }
  .values__item::before { content: ""; width: 7px; height: 7px; background: var(--brand-red); flex: none; }

  .qr { position: absolute; left: 448px; top: 178px; text-align: center; }
  .qr__code {
    width: 120px; height: 120px; background: var(--paper);
    border: 8px solid var(--paper); outline: 2px solid var(--charcoal-ink);
    background-image: linear-gradient(#d6d6d6, #d6d6d6);
  }
  .qr__caption { margin-top: 8px; font-size: 12px; color: var(--charcoal-text); letter-spacing: 1px; }

  .card--front .wordmark {
    position: absolute; left: 40px; top: 140px;
    font-size: 38px; color: var(--ink);
  }
  .card--front .wordmark__square { background: var(--brand-red); }

  .divider { position: absolute; background: var(--ink); width: 1px; left: 318px; top: 150px; height: 150px; }
  .divider--accent { background: var(--brand-red); width: 3px; top: 48px; height: 58px; left: 317px; }

  .contact { position: absolute; left: 340px; top: 44px; color: var(--ink); }
  .contact__cta { font-weight: 700; font-size: 25px; color: var(--brand-red); letter-spacing: 0.3px; }
  .contact__sub { font-size: 15px; margin-bottom: 40px; }
  .contact__line { display: flex; align-items: center; gap: 8px; font-size: 15px; line-height: 24px; }
  .contact__line svg { width: 14px; height: 14px; fill: var(--brand-red); flex: none; }
  .contact__address { font-size: 15px; line-height: 22px; margin-top: 10px; }
</style>
</head>
<body>
  <section class="card card--back" aria-label="Card back">
    <div class="wordmark">
      <div class="wordmark__square"></div>
      <div class="wordmark__name"><span>Corvalen</span><span>Technologies</span></div>
    </div>
    <ul class="values">
      <li class="values__title">Our values</li>
      <li class="values__item">Experience is Everything</li>
      <li class="values__item">Obsessed with Impossible</li>
      <li class="values__item">Consistency Over Time Equals Trust</li>
    </ul>
    <div class="qr">
      <div class="qr__code" role="img" aria-label="QR code linking to the support request page"></div>
      <div class="qr__caption">SCAN FOR SUPPORT</div>
    </div>
  </section>

  <section class="card card--front" aria-label="Card front">
    <div class="wordmark">
      <div class="wordmark__square"></div>
      <div class="wordmark__name"><span>Corvalen</span><span>Technologies</span></div>
    </div>
    <div class="divider divider--accent"></div>
    <div class="divider"></div>
    <div class="contact">
      <div class="contact__cta">Need IT support?</div>
      <div class="contact__sub">Scan, call or click.</div>
      <div class="contact__line">
        <svg viewBox="0 0 24 24"><path d="M6.6 10.8a15 15 0 0 0 6.6 6.6l2.2-2.2c.3-.3.7-.4 1-.2 1.1.4 2.3.6 3.6.6.6 0 1 .4 1 1V20c0 .6-.4 1-1 1A17 17 0 0 1 3 4c0-.6.4-1 1-1h3.5c.6 0 1 .4 1 1 0 1.3.2 2.5.6 3.6.1.3 0 .7-.2 1z"/></svg>
        (248) 555-0147
      </div>
      <div class="contact__line">
        <svg viewBox="0 0 24 24"><path d="M2 5h20v14H2z M2 5l10 8 10-8"/></svg>
        support@corvalenpc.com
      </div>
      <div class="contact__line">
        <svg viewBox="0 0 24 24"><circle cx="12" cy="12" r="10"/></svg>
        www.corvalenpc.com
      </div>
      <div class="contact__address">418 N Larkin Ave.<br>Ferndale, MI 48220</div>
    </div>
  </section>
</body>
</html>
```